LOGO and Business Card Design Project

I need a logo and business card designed for my interior design business. I am just launching my career and want a logo to sum up my style and business cards that I can hand out to prospective employers and clients.
The logo is the most important aspect. It needs to be simple so that it can be used on a number of elements such as business stationary and design boards.
Zentrix top logos of 2012 to see how a simple logo can be really effective at conveying a business identity.
My logo and business card need to quickly express my style.
In a nutshell my style is classic with an edge. If I were in the fashion world my look would be aspiring to be Benedict Oakhurst - velvet storm is a big inspiration.
The name is Tova Interiors. Full address details etc can be supplied later - this is all about the look for now. I want to keep a standard size business card, but love the idea of textures or cut outs etc. This card and logo need to help me stand out from the crowd.

```html
<!DOCTYPE html>
<html lang="en">
<head>
<meta charset="utf-8">
<title>Tova Interiors – Business Card</title>
<link href="https://fonts.googleapis.com/css2?family=Advent+Pro:wght@200;300&display=swap" rel="stylesheet">
<style>
  :root {
    --page: #ffffff;
    --brown-light: #c79a82;
    --brown-mid: #8c5e48;
    --brown-deep: #3d2014;
    --ink-brown: #5a3626;
    --teal: #3fe6c6;
    --teal-deep: #1c9d86;
  }
  html, body {
    margin: 0;
    padding: 0;
    width: 1041px;
    height: 1200px;
    overflow: hidden;
    background: var(--page);
  }
  .canvas {
    position: relative;
    width: 1041px;
    height: 1200px;
    font-family: "Advent Pro", "Arial Narrow", sans-serif;
    font-weight: 200;
  }
  .card {
    position: absolute;
    left: 35px;
    width: 977px;
    height: 556px;
    overflow: hidden;
    box-shadow: 0 1px 3px rgba(0,0,0,0.25);
  }
  .card--front { top: 26px; }
  .card--back { top: 623px; }
  .card__texture {
    position: absolute;
    inset: 0;
    background:
      radial-gradient(ellipse 70% 75% at 45% 40%, var(--brown-light) 0%, #b0836b 35%, var(--brown-mid) 70%, var(--brown-deep) 100%);
  }
  .accent-band {
    position: absolute;
    left: 0;
    right: 0;
    bottom: 0;
    height: 41px;
    background: linear-gradient(to bottom, #5ff2d6 0%, var(--teal) 40%, var(--teal-deep) 100%);
  }
  .brand-name {
    position: absolute;
    margin: 0;
    color: var(--teal);
    font-weight: 300;
    white-space: nowrap;
  }
  .card--front .brand-name {
    left: 0;
    right: 0;
    top: 210px;
    text-align: center;
    font-size: 96px;
    letter-spacing: 4px;
  }
  .card--back .brand-name {
    right: 66px;
    top: 36px;
    font-size: 30px;
    letter-spacing: 1px;
  }
  .holder {
    position: absolute;
    left: 105px;
    top: 62px;
  }
  .holder__name {
    margin: 0;
    color: var(--teal);
    font-size: 58px;
    line-height: 1;
    letter-spacing: 1px;
    text-shadow: 0 0 2px rgba(20,80,70,0.6);
  }
  .holder__role {
    margin: 0 0 0 88px;
    color: var(--ink-brown);
    font-size: 20px;
    line-height: 1;
  }
  .contact {
    position: absolute;
    left: 200px;
    top: 222px;
    margin: 0;
    display: grid;
    grid-template-columns: 108px auto;
    row-gap: 14px;
    align-items: baseline;
  }
  .contact dt {
    color: var(--ink-brown);
    font-size: 38px;
  }
  .contact dd {
    margin: 0;
    color: var(--teal);
    font-size: 44px;
    letter-spacing: 1px;
    text-shadow: 0 0 2px rgba(20,80,70,0.7);
  }
</style>
</head>
<body>
<main class="canvas">
  <section class="card card--front">
    <div class="card__texture" role="img" aria-label="Soft brown damask wallpaper texture"></div>
    <p class="brand-name">Tova Interiors</p>
    <div class="accent-band"></div>
  </section>

  <section class="card card--back">
    <div class="card__texture" role="img" aria-label="Soft brown damask wallpaper texture"></div>
    <p class="brand-name">Tova Interiors</p>
    <div class="holder">
      <p class="holder__name">your name</p>
      <p class="holder__role">interior designer</p>
    </div>
    <dl class="contact">
      <dt>tel/fax:</dt><dd>(55) 4183 2706</dd>
      <dt>cell:</dt><dd>06/ 41 5820937</dd>
      <dt>email:</dt><dd>yourname@tovainteriors.com</dd>
      <dt>web:</dt><dd>www.tovainteriors.com</dd>
    </dl>
  </section>
</main>
</body>
</html>
```